Australian Meat, Seafood and Fresh Produce Website

Our organization is looking to design a simple, but eye catching website to show our services.
Our company exports West Australian FRESH fruit and vegetables, seafood and meat.
The website we are looking for would consist of:
- Landing Page
- Company info
- Directors bio
- Page that highlights our products
- Contact us page
We would like it to have a Chinese translated version as well.
Tobin
Target Market(s)
Chinese Market
Industry/Entity Type
It Company
Number of Pages Required
1 page
Look and feel
Each slider illustrates characteristics of the customer's brand and the style your logo design should communicate.

```html
<!DOCTYPE html>
<html lang="en">
<head>
<meta charset="utf-8">
<title>Harbourline Fresh</title>
<link href="https://fonts.googleapis.com/css2?family=Raleway:wght@300;400;500;600;700&display=swap" rel="stylesheet">
<style>
:root{
  --red:#c8000f;
  --red-dark:#a6000a;
  --red-bright:#da0016;
  --ink:#222;
  --body:#444;
  --muted:#777;
  --pale:#f2f2f2;
  --btn-grey:#cfcfcf;
  --footer:#232323;
  --white:#fff;
}
*{margin:0;padding:0;box-sizing:border-box}
html,body{width:1200px;height:2176px;overflow:hidden}
body{font-family:'Raleway',sans-serif;color:var(--ink);background:var(--white);position:relative}
.abs{position:absolute}

/* header + hero */
.hero{position:absolute;left:0;top:0;width:1200px;height:522px;background:linear-gradient(90deg,#fafafa 0%,#f3f3f3 100%)}
.brand{position:absolute;left:87px;top:30px;display:flex;align-items:center;gap:14px}
.brand-dot{width:56px;height:56px;border-radius:50%;background:var(--red)}
.brand-name{font-size:34px;font-weight:400;color:var(--red);line-height:1}
.brand-tag{position:absolute;left:70px;top:40px;font-size:10px;color:var(--muted);letter-spacing:2.4px;white-space:nowrap}
.nav{position:absolute;top:53px;left:538px;display:flex;gap:0}
.nav a{font-size:13px;font-weight:500;color:var(--ink);text-decoration:none;margin-right:48px;letter-spacing:.3px}
.nav a.active{color:var(--red)}
.search{position:absolute;left:1095px;top:52px}
.hero-title{position:absolute;left:87px;top:140px;font-size:35px;font-weight:300;line-height:42px;letter-spacing:.5px;color:#333;width:520px}
.hero-title b{font-weight:500;color:var(--red)}
.btn{display:flex;align-items:center;justify-content:center;font-size:17px;font-weight:600;color:var(--white);border-radius:2px;letter-spacing:.3px}
.btn-red{background:linear-gradient(90deg,var(--red-dark),var(--red-bright))}
.btn-grey{background:var(--btn-grey);color:#f4f4f4}
.hero-btn{position:absolute;left:87px;top:345px;width:245px;height:44px}
.dots{position:absolute;left:87px;top:457px;display:flex;gap:5px}
.dots span{width:11px;height:11px;border-radius:50%;background:#c6c6c6}
.dots span.on{background:var(--red)}
.arrows{position:absolute;left:178px;top:450px;display:flex;gap:8px}
.hero-photo{position:absolute;left:515px;top:95px;width:685px;height:427px;
  background:radial-gradient(ellipse at 45% 55%,#c8491f 0%,#a9672d 35%,#6f9a3a 65%,rgba(243,243,243,0) 85%)}

/* products */
.products{position:absolute;left:0;top:522px;width:1200px;height:454px}
.product{position:absolute;top:0;width:300px;text-align:center}
.product-img{width:230px;height:180px;margin:61px auto 0;border-radius:50%}
.product h3{margin-top:45px;font-size:22px;font-weight:400;letter-spacing:.5px}
.product h3.hot{color:var(--red);font-weight:500}
.product p{margin:10px auto 0;width:280px;font-size:12.5px;font-weight:400;line-height:15.5px;color:var(--body)}

/* welcome */
.welcome{position:absolute;left:0;top:976px;width:1200px;height:418px;background:var(--pale);text-align:center}
.welcome-mark{width:56px;height:56px;border-radius:50%;background:var(--red);margin:53px auto 0}
.welcome h2{margin-top:22px;font-size:21px;font-weight:700;color:var(--red);letter-spacing:.3px}
.welcome p{width:650px;margin:22px auto 0;font-size:12.5px;line-height:21px;color:var(--body)}
.welcome-btns{position:absolute;left:347px;top:311px;display:flex;gap:8px}
.welcome-btns .btn{width:245px;height:44px}

/* team */
.team{position:absolute;left:0;top:1394px;width:1200px;height:378px;background:linear-gradient(180deg,var(--red-dark) 0%,var(--red-bright) 100%);color:var(--white)}
.team h2{position:absolute;top:56px;width:100%;text-align:center;font-size:21px;font-weight:600;letter-spacing:.3px}
.member{position:absolute;top:138px;width:236px;text-align:center}
.avatar{width:100px;height:100px;border-radius:50%;margin:0 auto;border:3px solid #f1f1f1;background:linear-gradient(180deg,#d9d9d9,#9a9a9a)}
.member h4{margin-top:14px;font-size:17px;font-weight:700}
.member span{display:block;margin-top:4px;font-size:10.5px;opacity:.9}

/* suppliers */
.suppliers{position:absolute;left:0;top:1772px;width:1200px;height:298px}
.suppliers h2{position:absolute;top:56px;width:100%;text-align:center;font-size:22px;font-weight:400;letter-spacing:.5px}
.supplier{position:absolute;top:146px;width:260px;font-size:22px;font-weight:700;text-align:center}

/* footer */
.footer{position:absolute;left:0;top:2070px;width:1200px;height:106px;background:var(--footer);color:var(--white)}
.footer-brand{position:absolute;left:87px;top:38px;display:flex;align-items:center;gap:8px;font-size:12px;font-weight:500}
.footer-brand i{width:30px;height:30px;border-radius:50%;background:var(--red);display:block}
.footer-nav{position:absolute;left:532px;top:46px;display:flex}
.footer-nav a{font-size:12.5px;color:#ccc;text-decoration:none;margin-right:48px}
.footer-nav a.active{color:var(--white);font-weight:700}
</style>
</head>
<body>

<header class="hero">
  <div class="hero-photo" role="img" aria-label="Wicker basket overflowing with fresh vegetables: broccoli, capsicum, tomatoes, cabbage, apples and onions"></div>
  <div class="brand">
    <div class="brand-dot"></div>
    <div class="brand-name">Harbourline Fresh</div>
    <div class="brand-tag">Supply high quality west australian produce</div>
  </div>
  <nav class="nav">
    <a class="active" href="#">HOME</a><a href="#">ABOUT US</a><a href="#">DIRECTORS</a><a href="#">PRODUCTS</a><a href="#">CONTACT US</a>
  </nav>
  <svg class="search" width="18" height="18" viewBox="0 0 18 18" fill="none" stroke="#333" stroke-width="1.6"><circle cx="7.5" cy="7.5" r="5.5"/><path d="M11.5 11.5L16 16"/></svg>
  <h1 class="hero-title">WE <b>AIMS</b> TO <b>SUPPLY HIGH QUALITY WEST</b> AUSTRALIAN PRODUCE TO THE REST OF THE WORLD.</h1>
  <a class="btn btn-red hero-btn">PRODUCTS</a>
  <div class="dots"><span></span><span></span><span class="on"></span><span></span></div>
  <div class="arrows">
    <svg width="24" height="24" viewBox="0 0 24 24"><circle cx="12" cy="12" r="11.5" fill="#d6d6d6"/><path d="M14 7l-5 5 5 5" stroke="#666" stroke-width="1.6" fill="none"/></svg>
    <svg width="24" height="24" viewBox="0 0 24 24"><circle cx="12" cy="12" r="11.5" fill="#e88a8a"/><path d="M10 7l5 5-5 5" stroke="#fff" stroke-width="1.6" fill="none"/></svg>
  </div>
</header>

<section class="products">
  <div class="product" style="left:103px">
    <div class="product-img" role="img" aria-label="Ripe red tomatoes, one cut in half" style="background:radial-gradient(circle,#d61a10 0%,#b81008 55%,rgba(255,255,255,0) 72%)"></div>
    <h3>FRUIT AND VEGETABLES</h3>
    <p>Western Australia is known for its high quality farming practices and environment, which produces meat, seafood, fruit and vegetable of a caliber that is respected globally.</p>
  </div>
  <div class="product" style="left:448px">
    <div class="product-img" role="img" aria-label="Pale peeled prawns" style="background:radial-gradient(circle,#fbe3dc 0%,#fdf0ec 55%,rgba(255,255,255,0) 72%)"></div>
    <h3 class="hot">SEAFOOD</h3>
    <p>Western Australia is known for its high quality farming practices and environment, which produces meat, seafood, fruit and vegetable of a caliber that is respected globally.</p>
  </div>
  <div class="product" style="left:793px">
    <div class="product-img" role="img" aria-label="Raw red beef cut with parsley" style="background:radial-gradient(circle,#c8525e 0%,#b23a48 50%,rgba(255,255,255,0) 72%)"></div>
    <h3>MEAT</h3>
    <p>Western Australia is known for its high quality farming practices and environment, which produces meat, seafood, fruit and vegetable of a caliber that is respected globally.</p>
  </div>
</section>

<section class="welcome">
  <div class="welcome-mark"></div>
  <h2>WELCOME TO HLF</h2>
  <p>Harbourline Fresh (HLF) aims to supply high quality West Australian produce to the rest of the World. Western Australia is known for its high quality farming practices and environment, which produces meat, seafood, fruit and vegetable of a caliber that is respected globally.<br>With a management team and first class suppliers allows our organization to provide quality ingredients, straight from farm or ocean to purchaser, in a timely manner to the highest quality.</p>
  <div class="welcome-btns">
    <a class="btn btn-red">PRODUCTS</a><a class="btn btn-grey">CONTACT US</a>
  </div>
</section>

<section class="team">
  <h2>THE MANAGEMENT TEAM</h2>
  <div class="member" style="left:127px"><div class="avatar" role="img" aria-label="Portrait photo of Jared Tobin"></div><h4>Jared Tobin</h4><span>Hospitality Management</span></div>
  <div class="member" style="left:364px"><div class="avatar" role="img" aria-label="Portrait photo of Owen Hartley" style="background:linear-gradient(180deg,#9a9a9a,#6a6a6a)"></div><h4>Owen Hartley</h4><span>Sales, Retail &amp; Procurement</span></div>
  <div class="member" style="left:600px"><div class="avatar" role="img" aria-label="Portrait photo of Colin Marsh"></div><h4>Colin Marsh</h4><span>Senior Executive</span></div>
  <div class="member" style="left:836px"><div class="avatar" role="img" aria-label="Portrait photo of Dr Mei Lin Zhou"></div><h4>Dr Mei Lin Zhou</h4><span>Senior Professional</span></div>
</section>

<section class="suppliers">
  <h2>OUR SUPPLIERS</h2>
  <div class="supplier" style="left:77px;color:#1a3f8f">Coralbay Seafoods</div>
  <div class="supplier" style="left:320px;color:#a89058">Greenvale</div>
  <div class="supplier" style="left:576px;color:#1a5f99">Ridgeway Meats</div>
  <div class="supplier" style="left:890px;width:260px;color:#1f4fa0">Southcross Meat Co.</div>
</section>

<footer class="footer">
  <div class="footer-brand"><i></i>© Copyright 2015. Harbourline Fresh. All Right Reserved.</div>
  <nav class="footer-nav">
    <a class="active" href="#">HOME</a><a href="#">ABOUT US</a><a href="#">DIRECTORS</a><a href="#">PRODUCTS</a><a href="#">CONTACT US</a><a href="#">POLICY</a>
  </nav>
</footer>

</body>
</html>
```